Yard signs to bring awareness to the neighborhood we are here to help you also.

My project is to build brand awareness in a Neighborhood before during and after my company's get a home owner approve from there in insurance Approved to replace there roof due to the recent storms. Call us we can do the same for you.
We are trying to let the neighborhood know that they may also have enough storm damage for them to have there roof and gutters replace at no cost to them. And we can help with there claim to go over all the steps involved.

Target Market(s)

Brand awareness to Home owner in the neighborhood

Industry/Entity Type

Roofing

Font styles to use
Sans Serif

Requirements
Must have
• Insurance Approved
Wind & Hail
Call For Free consultation
612 459-2817
Nice to have
• Make phone # big and bold

```html
<!DOCTYPE html>
<html lang="en">
<head>
<meta charset="utf-8">
<title>Insurance Approved Yard Sign</title>
<link rel="stylesheet" href="https://fonts.googleapis.com/css2?family=Bebas+Neue&family=Montserrat:wght@800&family=Lato:wght@700&family=Homemade+Apple&display=swap">
<style>
  :root {
    --backdrop: #535353;
    --teal: #0aaf97;
    --mint: #a9dccb;
    --script-green: #2fb89a;
    --royal-blue: #0c5da8;
    --black: #000000;
    --white: #ffffff;
  }
  html, body {
    margin: 0;
    padding: 0;
    width: 1200px;
    height: 2168px;
    overflow: hidden;
    background: var(--backdrop);
  }
  .yard-sign {
    position: absolute;
    left: 164px;
    top: 154px;
    width: 868px;
    height: 649px;
    background: var(--black);
    overflow: hidden;
  }
  .headline-band {
    position: absolute;
    left: 0; top: 0;
    width: 868px;
    height: 154px;
    background: var(--teal);
    border-radius: 0 0 84px 84px;
  }
  .headline {
    position: absolute;
    left: 0; top: 6px;
    width: 868px;
    margin: 0;
    text-align: center;
    font-family: "Bebas Neue", sans-serif;
    font-weight: 400;
    font-size: 113px;
    line-height: 1;
    letter-spacing: 0;
    color: var(--black);
    transform: scaleY(1.02);
  }
  .peril-tag {
    position: absolute;
    left: 225px; top: 115px;
    width: 447px; height: 69px;
  }
  .peril-tag svg { position: absolute; inset: 0; }
  .peril-tag span {
    position: absolute;
    inset: 0;
    display: flex;
    align-items: center;
    justify-content: center;
    font-family: "Montserrat", sans-serif;
    font-weight: 800;
    font-size: 55px;
    color: var(--white);
    letter-spacing: -1px;
  }
  .company-name {
    position: absolute;
    left: 0; top: 196px;
    width: 868px;
    margin: 0;
    text-align: center;
    font-family: "Bebas Neue", sans-serif;
    font-weight: 400;
    font-size: 88px;
    line-height: 1;
    color: var(--mint);
  }
  .brand-square {
    position: absolute;
    left: 158px; top: 314px;
    width: 80px; height: 80px;
    background: var(--teal);
  }
  .tagline {
    position: absolute;
    margin: 0;
    font-family: "Homemade Apple", cursive;
    font-size: 34px;
    line-height: 1;
    color: var(--script-green);
    white-space: nowrap;
  }
  .tagline.first { left: 248px; top: 336px; }
  .tagline.second { left: 312px; top: 380px; }
  .contact-panel {
    position: absolute;
    left: 0; top: 447px;
    width: 868px; height: 202px;
    background: var(--white);
  }
  .call-prompt {
    position: absolute;
    left: 0; top: 14px;
    width: 868px;
    margin: 0;
    text-align: center;
    font-family: "Lato", sans-serif;
    font-weight: 700;
    font-size: 40px;
    line-height: 1;
    color: var(--royal-blue);
  }
  .phone-icon {
    position: absolute;
    left: 82px; top: 85px;
    width: 86px; height: 86px;
  }
  .phone-number {
    position: absolute;
    left: 196px; top: 62px;
    margin: 0;
    font-family: "Bebas Neue", sans-serif;
    font-weight: 400;
    font-size: 136px;
    line-height: 1;
    color: var(--royal-blue);
    letter-spacing: 1px;
    white-space: nowrap;
  }
</style>
</head>
<body>
  <main class="yard-sign">
    <div class="headline-band"></div>
    <h1 class="headline">Insurance Approved</h1>

    <div class="peril-tag">
      <svg viewBox="0 0 447 69" width="447" height="69" aria-hidden="true">
        <polygon points="14,0 447,0 432,69 0,69" fill="var(--royal-blue)"/>
      </svg>
      <span>WIND &amp; HAIL</span>
    </div>

    <h2 class="company-name">J&amp;R ROOFING LLC.</h2>

    <div class="brand-square" aria-hidden="true"></div>
    <p class="tagline first">Nobody Does it Better!</p>
    <p class="tagline second">Here To Serve.</p>

    <section class="contact-panel">
      <p class="call-prompt">Call For Free consultation</p>
      <svg class="phone-icon" viewBox="0 0 24 24" aria-hidden="true">
        <path fill="var(--royal-blue)" d="M6.6 2.2c.6-.4 1.4-.3 1.8.3l2.2 3.4c.4.6.3 1.3-.2 1.8L8.9 9.1c1.2 2.6 3.3 4.7 6 6l1.4-1.5c.5-.5 1.2-.6 1.8-.2l3.4 2.2c.6.4.8 1.2.3 1.8l-1.6 2.3c-.7 1-2 1.4-3.1 1C10.7 18.6 5.4 13.3 3.3 7c-.4-1.1 0-2.4 1-3.1z"/>
        <path fill="none" stroke="var(--royal-blue)" stroke-width="1.8" stroke-linecap="round" d="M13.5 6.3a4.4 4.4 0 0 1 4.2 4.2"/>
        <path fill="none" stroke="var(--royal-blue)" stroke-width="1.8" stroke-linecap="round" d="M13.8 2.4a8.2 8.2 0 0 1 7.8 7.8"/>
      </svg>
      <p class="phone-number">612 459-2817</p>
    </section>
  </main>
</body>
</html>
```